Birch Hollow Lodge & Harbour. A site that will sell our lifestyle and embody our vision.

We are after a fun interactive website for our property development.
Check out our ideas for layout and content.
Use stock videos and phots if we havent provide enough.
Ive attached our Logo.
We are easy to reach and work with. Love the crative process.1.Our Vision.. (This clicks through to vision page)
Nestled in the North East corner of Tesko Lake , Sk amidst thousands of acres of natural beauty, a unique community is taking shape. A community that connectS people, nature and play. A place to find those simpler times.

2.Explore..(This clicks through to explore page)
Discover a new life of adventure, on the lake fishing, in the bush on our trail system or maybe the local golf course.

3. Live Here..(This through to Live page)
Birch Hollow has everything you need to start living a full life based in a thriving community.
Slow down and get to know nature and your neighbors

Target Market(s)

35-65 Lake Life

Coding

Coded - Design and coding required

Number of Pages Required

5+ page

Font styles to use
Other font styles liked:
• Anntonio

Colors
00AB8E
00BBA5
67D7C9
C6EFE9
E9F9F6
F0912C
F2A743
F7CA91
FBE8D2
FDF5EE

Requirements
Nice to have
• Interactive

```html
<!DOCTYPE html>
<html lang="en">
<head>
<meta charset="utf-8">
<title>Birch Hollow Lodge &amp; Harbour</title>
<link href="https://fonts.googleapis.com/css2?family=Antonio:wght@300;400;500;600;700&display=swap" rel="stylesheet">
<style>
:root{
  --ink:#111111;
  --white:#ffffff;
  --green:#4b5e17;
  --blue:#1c3a62;
  --brown:#5c3312;
  --muted:#6f6f6f;
  --slate:#5878a0;
  --line:#c9c9c9;
  --teal-900:#00AB8E;
  --teal-700:#00BBA5;
  --teal-400:#67D7C9;
  --teal-200:#C6EFE9;
  --teal-50:#E9F9F6;
  --orange-900:#F0912C;
  --orange-700:#F2A743;
  --orange-400:#F7CA91;
  --orange-200:#FBE8D2;
  --orange-50:#FDF5EE;
}
*{box-sizing:border-box;margin:0;padding:0}
html,body{width:1200px;height:5034px;overflow:hidden}
body{position:relative;background:var(--white);font-family:"Antonio",sans-serif;color:var(--ink)}
.abs{position:absolute}

/* hero */
.hero-photo{position:absolute;left:0;top:0;width:1200px;height:590px}
.nav-bar{position:absolute;left:0;top:94px;width:1200px;height:54px;background:var(--ink);border-top:3px solid var(--white);border-bottom:3px solid var(--white)}
.nav-links{position:absolute;left:74px;top:112px;font-size:12px;color:var(--white)}
.nav-links a{color:var(--white);text-decoration:none;position:absolute;white-space:nowrap}
.nav-contact{position:absolute;top:113px;font-size:11px;color:var(--white);display:flex;align-items:center;gap:6px;white-space:nowrap}
.brand-badge{position:absolute;left:490px;top:10px;width:220px;height:220px;border-radius:50%;background:var(--ink);border:5px solid var(--white);display:flex;flex-direction:column;align-items:center;justify-content:center;color:var(--white)}
.brand-badge .mark{width:22px;height:22px;background:var(--white);margin-bottom:14px}
.brand-badge .name{font-size:24px;font-weight:500;letter-spacing:1px;line-height:1.1}
.brand-badge .sub{font-size:10px;letter-spacing:2px;margin-top:6px}
.hero-title{position:absolute;left:0;width:1200px;top:315px;text-align:center;font-size:86px;font-weight:500;color:var(--white);letter-spacing:1px;line-height:1}
.hero-arrow{position:absolute;top:541px;width:40px;height:40px;border-radius:50%;background:rgba(255,255,255,.8);display:flex;align-items:center;justify-content:center}

/* soft section backdrops */
.backdrop{position:absolute;left:0;width:1200px}
.bd-orange{background:linear-gradient(180deg,var(--white) 0%,var(--orange-50) 45%,var(--orange-200) 100%)}
.bd-teal{background:linear-gradient(180deg,var(--white) 0%,var(--teal-50) 45%,var(--teal-200) 100%)}
.bd-fade{position:absolute;left:0;width:1200px;height:60px;background:linear-gradient(180deg,rgba(255,255,255,0),var(--white))}

/* intro cards */
.card{position:absolute;width:310px;height:318px;top:684px;border-radius:16px}
.card-inner{position:absolute;left:20px;right:20px;top:43px;bottom:21px;border-radius:14px;border:1.5px solid}
.card-title{position:absolute;left:20px;top:-26px;padding:0 8px;font-size:40px;font-weight:500;line-height:1.1;text-transform:uppercase}
.card-body{position:absolute;left:26px;right:26px;top:38px;font-size:13px;line-height:1.15;color:var(--muted);text-align:justify;font-weight:300}
.card-btn{position:absolute;left:26px;right:26px;top:180px;height:36px;border-radius:3px;color:var(--white);font-size:10px;font-weight:600;display:flex;align-items:center;justify-content:center;letter-spacing:.5px}
.tint-green{background:rgba(190,200,172,.85)}
.tint-blue{background:rgba(184,196,218,.9)}
.tint-brown{background:rgba(214,200,188,.9)}
.in-green{background:#dde3d2;border-color:var(--green)}
.in-blue{background:#dbe1ec;border-color:var(--blue)}
.in-brown{background:#ebe2d9;border-color:var(--brown)}

/* section heads */
.sec-head{position:absolute;left:0;width:1200px;text-align:center;font-size:56px;font-weight:500;line-height:1;text-transform:uppercase}
.sec-lede{position:absolute;left:200px;width:800px;text-align:center;font-size:14px;line-height:1.25;color:var(--muted);font-weight:300}
.photo{position:absolute;left:104px;width:994px;height:458px;border-radius:22px}

/* feature cards */
.feat{position:absolute;width:310px;height:304px;border-radius:16px;background:rgba(255,255,255,.6)}
.feat-inner{position:absolute;left:20px;right:20px;top:30px;bottom:20px;background:var(--white);border:1.5px solid var(--line);border-radius:14px}
.feat-title{position:absolute;left:20px;top:-14px;background:var(--white);padding:0 8px;font-size:25px;line-height:1.05;font-weight:500;max-width:230px}
.feat-body{position:absolute;left:26px;right:26px;font-size:13px;line-height:1.15;color:var(--muted);text-align:justify;font-weight:300}

/* time cards */
.time{position:absolute;top:2941px;width:224px;height:209px;border-radius:16px;background:rgba(255,255,255,.6)}
.time-inner{position:absolute;left:22px;right:22px;top:20px;bottom:20px;background:var(--white);border:1.5px solid var(--line);border-radius:12px}
.time-tag{position:absolute;left:14px;top:-16px;background:var(--white);padding:0 8px;display:flex;align-items:center;gap:8px;font-size:26px;font-weight:500;color:var(--blue);line-height:1.2}
.time-place{position:absolute;left:0;right:0;top:66px;text-align:center;font-size:26px;line-height:1.05;color:var(--slate)}

/* form */
.field{position:absolute;border:1.5px solid var(--line);border-radius:8px;font-size:10px;color:#888;padding:14px 16px;background:var(--white)}
.submit{position:absolute;left:492px;top:4727px;width:215px;height:36px;background:var(--green);color:var(--white);font-size:11px;font-weight:600;display:flex;align-items:center;justify-content:center;border-radius:2px}

/* footer */
.footer{position:absolute;left:0;top:4799px;width:1200px;height:235px;background:var(--ink);color:var(--white)}
.footer-brand{position:absolute;left:130px;top:60px;width:150px;text-align:center}
.footer-brand .mark{width:22px;height:22px;background:var(--white);margin:0 auto 14px}
.footer-brand .name{font-size:22px;font-weight:500;line-height:1.1}
.footer-brand .sub{font-size:9px;letter-spacing:2px;margin-top:6px}
.foot-link{position:absolute;left:420px;font-size:12px}
.foot-follow{position:absolute;left:668px;top:62px;font-size:12px}
.social{position:absolute;top:96px;width:14px;height:14px;border:1.5px solid var(--white);border-radius:50%}
.foot-contact{position:absolute;left:905px;font-size:11px;display:flex;align-items:center;gap:8px;white-space:nowrap}
</style>
</head>
<body>

<!-- HERO -->
<svg class="hero-photo" viewBox="0 0 1200 590" role="img" aria-label="Photo of a lakeside lodge on green lawns under a cloudy sky, reflected in calm water with docks">
  <defs>
    <linearGradient id="heroGrad" x1="0" y1="0" x2="0" y2="1">
      <stop offset="0" stop-color="#b9bfc6"/>
      <stop offset="0.35" stop-color="#dfe2e4"/>
      <stop offset="0.55" stop-color="#6f8a3e"/>
      <stop offset="0.75" stop-color="#4e6a2c"/>
      <stop offset="1" stop-color="#5d7474"/>
    </linearGradient>
  </defs>
  <path d="M0 0H1200V440Q600 740 0 440Z" fill="url(#heroGrad)"/>
</svg>

<div class="nav-bar"></div>
<nav class="nav-links">
  <a style="left:0">Home</a>
  <a style="left:49px">Our Vision</a>
  <a style="left:119px">Explore</a>
  <a style="left:178px">Live Here</a>
  <a style="left:244px">Contact Us</a>
</nav>
<div class="nav-contact" style="left:893px">
  <svg width="14" height="11" viewBox="0 0 14 11"><rect x="0.75" y="0.75" width="12.5" height="9.5" fill="none" stroke="#fff" stroke-width="1.3"/><path d="M1 1l6 5 6-5" fill="none" stroke="#fff" stroke-width="1.3"/></svg>
  hello@birchhollow.example
</div>
<div class="nav-contact" style="left:1032px">
  <svg width="12" height="12" viewBox="0 0 24 24"><path fill="#fff" d="M6.6 10.8a15.1 15.1 0 006.6 6.6l2.2-2.2a1 1 0 011-.25 11.4 11.4 0 003.6.57 1 1 0 011 1V20a1 1 0 01-1 1A17 17 0 013 4a1 1 0 011-1h3.5a1 1 0 011 1c0 1.25.2 2.45.57 3.57a1 1 0 01-.25 1z"/></svg>
  0330 555 019 2040
</div>

<div class="brand-badge">
  <div class="mark"></div>
  <div class="name">BIRCH HOLLOW</div>
  <div class="sub">LODGE &amp; HARBOUR</div>
</div>

<h1 class="hero-title">CONNECT TO NATURE</h1>
<div class="hero-arrow" style="left:551px"><svg width="14" height="14" viewBox="0 0 14 14"><path d="M9 2L4 7l5 5" fill="none" stroke="#333" stroke-width="2"/></svg></div>
<div class="hero-arrow" style="left:609px"><svg width="14" height="14" viewBox="0 0 14 14"><path d="M5 2l5 5-5 5" fill="none" stroke="#333" stroke-width="2"/></svg></div>

<!-- INTRO CARDS -->
<div class="backdrop bd-orange" style="top:600px;height:470px" role="img" aria-label="Soft misty pine forest backdrop"></div>
<div class="bd-fade" style="top:1040px"></div>

<div class="card tint-green" style="left:104px">
  <div class="card-inner in-green">
    <div class="card-title in-green" style="color:var(--green)">Our Vision</div>
    <p class="card-body">Nestled in the North East corner of Tesko Lake , Sk amidst thousands of acres of natural beauty, a unique community is taking shape. A community that connects people, nature and play. A place to find those simpler times.</p>
    <div class="card-btn" style="background:var(--green)">KNOW MORE</div>
  </div>
</div>
<div class="card tint-blue" style="left:446px">
  <div class="card-inner in-blue">
    <div class="card-title in-blue" style="color:var(--blue)">Explore</div>
    <p class="card-body">Discover a new life of adventure, on the lake fishing, in the bush on our trail system or maybe the local golf course.</p>
    <div class="card-btn" style="background:var(--blue)">KNOW MORE</div>
  </div>
</div>
<div class="card tint-brown" style="left:786px">
  <div class="card-inner in-brown">
    <div class="card-title in-brown" style="color:var(--brown)">Live Here</div>
    <p class="card-body">Birch Hollow has everything you need to start living a full life based in a thriving community.<br><br>Slow down and get to know nature and your neighbors</p>
    <div class="card-btn" style="background:var(--brown)">KNOW MORE</div>
  </div>
</div>

<!-- OUR VISION -->
<h2 class="sec-head" style="top:1152px;color:var(--green)">Our Vision</h2>
<p class="sec-lede" style="top:1223px">Nestled in the North East corner of Tesko Lake , Sk amidst thousands of acres of natural beauty, a unique community is taking shape. A community that connects people, nature and play. A place to find those simpler times.</p>
<div class="photo" style="top:1292px;background:linear-gradient(135deg,#e9e6df 0%,#d6d2c9 45%,#a89a84 70%,#5d5a55 100%)" role="img" aria-label="Photo of a planner drawing on a scale model of the lakeside community with compass and ruler"></div>

<div class="backdrop bd-teal" style="top:1759px;height:450px" role="img" aria-label="Soft misty pine forest backdrop"></div>
<div class="bd-fade" style="top:2180px"></div>

<div class="feat" style="left:104px;top:1807px">
  <div class="feat-inner">
    <div class="feat-title" style="color:var(--green)">Building Community</div>
    <p class="feat-body" style="top:38px">Nestled on the banks of Tesko Lake, Birch Hollow is home to a multitude of cultures, a vibrant fishing community, a lake golf course, and around 320 days of sunshine.</p>
  </div>
</div>
<div class="feat" style="left:446px;top:1807px">
  <div class="feat-inner">
    <div class="feat-title" style="color:var(--green)">Connecting People, Nature, And Play</div>
    <p class="feat-body" style="top:64px">Founded in 1973 with a vision of paving a road to the play ground of the north, Birch Hollow is responsible for Tesko Lake's most iconic and transformative projects, we always invest with purpose while positively impacting community. Birch Hollow is expected to have people by 2027, with homes and acres of community reserves.</p>
  </div>
</div>
<div class="feat" style="left:786px;top:1807px">
  <div class="feat-inner">
    <div class="feat-title" style="color:var(--green)">Driven By Purpose</div>
    <p class="feat-body" style="top:38px">Our transformative community planning has created a ecosystem of amenities and services that enhance lives and ensure the area will grow and thrive for generations to come, we always invest with purpose.</p>
  </div>
</div>

<!-- EXPLORE -->
<h2 class="sec-head" style="top:2284px;color:var(--blue)">Explore</h2>
<p class="sec-lede" style="top:2352px">Discover a new life of adventure, on the lake fishing, in the bush on our trail system or maybe the local golf course.</p>
<div class="photo" style="top:2423px;background:linear-gradient(180deg,#f2f2f0 0%,#b8893a 22%,#6f6a33 40%,#cfd3d4 55%,#9aa0a2 75%,#4a3a2c 100%)" role="img" aria-label="Photo of two people fishing from a wooden dock on a calm lake lined with autumn trees"></div>

<div class="backdrop bd-teal" style="top:2892px;height:340px" role="img" aria-label="Soft misty pine forest backdrop"></div>
<div class="bd-fade" style="top:3200px"></div>

<div class="time" style="left:104px"><div class="time-inner">
  <div class="time-tag"><svg width="26" height="26" viewBox="0 0 26 26"><circle cx="13" cy="13" r="11" fill="none" stroke="#1c3a62" stroke-width="2.5"/><path d="M13 6v7l4 3" fill="none" stroke="#1c3a62" stroke-width="2.5"/></svg>10min</div>
  <div class="time-place">Dockside<br>IceCream</div>
</div></div>
<div class="time" style="left:360px"><div class="time-inner">
  <div class="time-tag"><svg width="26" height="26" viewBox="0 0 26 26"><circle cx="13" cy="13" r="11" fill="none" stroke="#1c3a62" stroke-width="2.5"/><path d="M13 6v7l4 3" fill="none" stroke="#1c3a62" stroke-width="2.5"/></svg>15min</div>
  <div class="time-place">Heron Ridge<br>Golf Course</div>
</div></div>
<div class="time" style="left:616px"><div class="time-inner">
  <div class="time-tag"><svg width="26" height="26" viewBox="0 0 26 26"><circle cx="13" cy="13" r="11" fill="none" stroke="#1c3a62" stroke-width="2.5"/><path d="M13 6v7l4 3" fill="none" stroke="#1c3a62" stroke-width="2.5"/></svg>20min</div>
  <div class="time-place">Cedar<br>Narrows</div>
</div></div>
<div class="time" style="left:872px"><div class="time-inner">
  <div class="time-tag"><svg width="26" height="26" viewBox="0 0 26 26"><circle cx="13" cy="13" r="11" fill="none" stroke="#1c3a62" stroke-width="2.5"/><path d="M13 6v7l4 3" fill="none" stroke="#1c3a62" stroke-width="2.5"/></svg>45min</div>
  <div class="time-place">Willow Flats<br>Provincial Park</div>
</div></div>

<!-- LIVE HERE -->
<h2 class="sec-head" style="top:3308px;color:var(--brown)">Live Here</h2>
<p class="sec-lede" style="top:3376px">Birch Hollow has everything you need to start living a full life based in a thriving community.<br>Slow down and get to know nature and your neighbors</p>
<div class="photo" style="top:3447px;background:linear-gradient(180deg,#9fb3c8 0%,#4e6f86 22%,#1f3d2c 45%,#264a3a 60%,#3d7a86 78%,#1d4856 100%)" role="img" aria-label="Photo of a lodge on the shore of a still mountain lake surrounded by dense evergreen forest"></div>

<div class="backdrop bd-orange" style="top:3918px;height:410px" role="img" aria-label="Soft misty pine forest backdrop"></div>
<div class="bd-fade" style="top:4300px"></div>

<div class="feat" style="left:104px;top:3957px">
  <div class="feat-inner">
    <div class="feat-title" style="color:var(--brown)">Picture yourself here</div>
    <p class="feat-body" style="top:38px">A dynamic mix of land choices and a range of price points mean anyone and everyone can live their very best lives when they call Birch Hollow home</p>
  </div>
</div>
<div class="feat" style="left:446px;top:3957px">
  <div class="feat-inner">
    <div class="feat-title" style="color:var(--brown)">No Building restrictions</div>
    <p class="feat-body" style="top:64px">Homes in Birch Hollow are built with an eclectic mix of complementary and distinctive architecture styles and sizes. Combined with thoughtful urban planning, these homes will form a progressive, timeless community that better mimics organic neighbourhoods built over decades - rather than cookie-cutter to a single style.</p>
  </div>
</div>
<div class="feat" style="left:786px;top:3957px">
  <div class="feat-inner">
    <div class="feat-title" style="color:var(--brown)">Find A builder</div>
    <div class="abs" style="left:34px;top:58px;display:flex;align-items:center;gap:12px">
      <div style="width:34px;height:34px;background:var(--brown)"></div>
      <div style="font-size:22px;font-weight:600;line-height:1;color:var(--ink)">RIDGELINE<br>CONSTRUCTION</div>
    </div>
    <div class="abs" style="left:0;right:0;top:136px;text-align:center;font-size:36px;font-weight:500;color:var(--ink)">The Timberhands</div>
  </div>
</div>

<!-- GET IN TOUCH -->
<h2 class="sec-head" style="top:4418px;color:var(--green)">Get In Touch</h2>
<div class="field" style="left:123px;top:4506px;width:303px;height:47px">Your Name</div>
<div class="field" style="left:449px;top:4506px;width:301px;height:47px">Email</div>
<div class="field" style="left:774px;top:4506px;width:303px;height:47px">Phone</div>
<div class="field" style="left:123px;top:4588px;width:954px;height:106px">Your message</div>
<div class="submit">SUBMIT MASSAGE</div>

<!-- FOOTER -->
<footer class="footer">
  <div class="footer-brand">
    <div class="mark"></div>
    <div class="name">BIRCH HOLLOW</div>
    <div class="sub">LODGE &amp; HARBOUR</div>
  </div>
  <div class="foot-link" style="top:62px">Our Vision</div>
  <div class="foot-link" style="top:95px">Explore</div>
  <div class="foot-link" style="top:128px">Live Here</div>
  <div class="foot-link" style="top:159px">Contact Us</div>
  <div class="foot-follow">Follow Us</div>
  <div class="social" style="left:652px"></div>
  <div class="social" style="left:684px"></div>
  <div class="social" style="left:716px"></div>
  <div class="foot-contact" style="top:62px">
    <svg width="12" height="12" viewBox="0 0 24 24"><path fill="#fff" d="M6.6 10.8a15.1 15.1 0 006.6 6.6l2.2-2.2a1 1 0 011-.25 11.4 11.4 0 003.6.57 1 1 0 011 1V20a1 1 0 01-1 1A17 17 0 013 4a1 1 0 011-1h3.5a1 1 0 011 1c0 1.25.2 2.45.57 3.57a1 1 0 01-.25 1z"/></svg>
    0330 555 019 2040
  </div>
  <div class="foot-contact" style="top:95px">
    <svg width="14" height="11" viewBox="0 0 14 11"><rect x="0.75" y="0.75" width="12.5" height="9.5" fill="none" stroke="#fff" stroke-width="1.3"/><path d="M1 1l6 5 6-5" fill="none" stroke="#fff" stroke-width="1.3"/></svg>
    hello@birchhollow.example
  </div>
  <div class="foot-contact" style="top:126px">
    <svg width="12" height="14" viewBox="0 0 12 14"><path d="M6 13S1 8 1 5a5 5 0 0110 0c0 3-5 8-5 8z" fill="none" stroke="#fff" stroke-width="1.3"/><circle cx="6" cy="5" r="1.7" fill="#fff"/></svg>
    1234 Street Name, City Name
  </div>
</footer>

</body>
</html>
```